Marcus Pellow Carpentry & Joinery

Hello, I would like a flyer designed for my new business doing small projects in my local area for home-owners. I am a professional tradesman.
The type of work I am offering is:
- decks/decking
- external stairs & railings
- install windows & doors
- roofs & gutters
- small additions
- built-in wardrobes
- finish work
- demolition

It would be great if the flyer could mention these, or use phrasing that fits this kind of construction work.
My idea for a slogan was "new work and repairs to any age home".

Please also mention FREE QUOTES and have my email and phone number included on the flyer, along with my carpentry licence number, which I can provided.

I'd like a one page, single-sided flyer that could be printed as DL.
Colour and style is up to you! I'll be placing this flyer on counters & in the windows of local businesses, so something simple and eye-catching is preferred.

Thank you!

```html
<!DOCTYPE html>
<html lang="en">
<head>
<meta charset="UTF-8">
<title>Marcus Pellow Carpentry &amp; Joinery – Flyer</title>
<link rel="stylesheet" href="https://fonts.googleapis.com/css2?family=Alfa+Slab+One&display=swap">
<style>
  :root {
    --wood-light: #eaa64c;
    --wood-dark: #d58a32;
    --maroon: #7c1414;
    --maroon-deep: #5a1208;
    --white: #ffffff;
    --ink: #2a1404;
    --photo-light: #8a8d92;
    --photo-dark: #4a5570;
  }
  * { margin: 0; padding: 0; box-sizing: border-box; }
  html, body { width: 848px; height: 1200px; overflow: hidden; background: #ffffff; }
  .flyer {
    position: relative;
    width: 848px;
    height: 1200px;
    overflow: hidden;
    font-family: "Alfa Slab One", "Rockwell", serif;
  }
  .wood-backdrop {
    position: absolute;
    inset: 0;
    background: linear-gradient(100deg, var(--wood-dark) 0%, var(--wood-light) 55%, var(--wood-dark) 100%);
  }
  .tradesman-photo {
    position: absolute;
    left: 0; top: 0;
    width: 220px; height: 1200px;
    background: linear-gradient(180deg, var(--photo-light) 0%, var(--photo-dark) 100%);
  }
  .headline {
    position: absolute;
    left: 280px; top: 40px;
    width: 540px;
    text-align: center;
    color: var(--white);
    font-size: 72px;
    font-weight: 400;
    font-style: italic;
    line-height: 84px;
    transform: rotate(-4deg);
    text-shadow:
      3px 3px 0 var(--maroon-deep), -3px -3px 0 var(--maroon-deep),
      3px -3px 0 var(--maroon-deep), -3px 3px 0 var(--maroon-deep),
      6px 6px 0 var(--maroon-deep);
  }
  .services {
    position: absolute;
    right: 35px; top: 404px;
    list-style: none;
    text-align: right;
    color: var(--maroon);
    font-size: 43px;
    line-height: 48px;
    white-space: nowrap;
    text-shadow:
      2px 2px 0 var(--white), -2px -2px 0 var(--white),
      2px -2px 0 var(--white), -2px 2px 0 var(--white);
  }
  .free-quotes {
    position: absolute;
    right: 35px; top: 798px;
    color: var(--maroon-deep);
    font-size: 56px;
    letter-spacing: 3px;
    text-shadow: 2px 2px 0 #f2c47f, -1px -1px 0 #f2c47f;
  }
  .call-band {
    position: absolute;
    left: 273px; top: 884px;
    width: 575px; height: 200px;
    background: var(--maroon);
    color: var(--white);
    padding: 4px 35px 0 0;
    text-align: right;
  }
  .call-band .line { display: block; font-size: 104px; line-height: 92px; letter-spacing: 2px; white-space: nowrap; }
  .call-band .label { font-size: 60px; letter-spacing: 0; }
  .email {
    position: absolute;
    right: 35px; top: 1090px;
    color: var(--white);
    font-size: 27px;
    text-shadow:
      2px 2px 0 var(--maroon-deep), -2px -2px 0 var(--maroon-deep),
      2px -2px 0 var(--maroon-deep), -2px 2px 0 var(--maroon-deep);
  }
  .licence {
    position: absolute;
    right: 35px; top: 1143px;
    color: var(--ink);
    font-size: 22px;
    text-shadow: 1px 1px 0 var(--white), -1px -1px 0 var(--white), 1px -1px 0 var(--white), -1px 1px 0 var(--white);
  }
</style>
</head>
<body>
<main class="flyer">
  <div class="wood-backdrop" role="img" aria-label="Backdrop of vertical golden timber planks fixed with nails"></div>

  <div class="tradesman-photo" role="img" aria-label="Photo of a tradesman with crossed arms wearing a grey work shirt, jeans and a leather tool belt holding hand tools"></div>

  <h1 class="headline">New work and repairs to any age home!</h1>

  <ul class="services">
    <li>Decks/decking</li>
    <li>External stairs &amp; railings</li>
    <li>Install windows &amp; doors</li>
    <li>Roofs &amp; gutters</li>
    <li>Small additions</li>
    <li>Built-in wardrobes</li>
    <li>Finish work</li>
    <li>Demolition</li>
  </ul>

  <p class="free-quotes">FREE QUOTES</p>

  <div class="call-band">
    <span class="line"><span class="label">Call: </span>0412</span>
    <span class="line">555 208</span>
  </div>

  <p class="email">marcuspellow15@inboxmail.com</p>
  <p class="licence">BCA Licence number: 1304528</p>
</main>
</body>
</html>
```